Postcard Design

We are a licensed and insured remodeling contractor in Johnson County, KS. I am looking to get a professional look for our postcard advertising. I would prefer something that appeals to women, but is still masculine enough for a contractor. Here is the verbiage I would like in the postcard.
Ever question the references you get from a contractor? Wouldn't you prefer to get a reference from your neighbor?
We are currently working with one of your neighbors and would love the opportunity to work for you. You can look us up on our website and see some of the wonderful spaces we have helped create. Call us today to schedule an appointment and let us know how we can help you create the new space you have always dreamed of.
Tel: 555-302-1186
Fax:555-317-2094
WWW.BELTRIDGEHOMEWORKS.EXAMPLE
BELTRIDGEHOMEWORKS@MAILBOXLY.EXAMPLE
Here is the verbiage I would like to use.
We are working in your neighborhood.
Tel: 555-302-1186
Fax:555-317-2094

```html
<!DOCTYPE html>
<html lang="en">
<head>
<meta charset="utf-8">
<title>Beltridge Home Works — Neighborhood Postcard</title>
<link rel="stylesheet" href="https://fonts.googleapis.com/css2?family=Exo+2:ital,wght@0,400;0,500;0,600;0,700;1,400;1,500;1,600&display=swap">
<style>
  :root {
    --navy: #1e2c3c;
    --navy-deep: #15202d;
    --navy-soft: #2c3d50;
    --orange: #ec9a2e;
    --orange-deep: #d9861c;
    --paper: #ffffff;
    --mist: #d6d9dd;
    --ink: #1b2430;
    --stage: #ece7df;
  }
  * { box-sizing: border-box; margin: 0; padding: 0; }
  html, body { width: 1200px; height: 800px; overflow: hidden; }
  body {
    background: var(--stage);
    font-family: "Exo 2", "Trebuchet MS", sans-serif;
    position: relative;
  }

  .card {
    position: absolute;
    width: 540px;
    overflow: hidden;
    box-shadow: 0 6px 18px rgba(0,0,0,0.18);
    background: var(--paper);
  }

  /* ---------- Front ---------- */
  .card--front { left: 40px; top: 60px; height: 500px; }
  .front-header {
    height: 212px;
    background: linear-gradient(180deg, #ffffff 0%, #f1f2f3 55%, var(--mist) 100%);
    display: flex; align-items: center; justify-content: center;
    padding-bottom: 30px;
  }
  .brand {
    display: flex; align-items: center; gap: 12px;
    font-weight: 600; font-size: 34px; color: var(--navy);
    letter-spacing: 1px; white-space: nowrap;
  }
  .brand-mark { width: 26px; height: 26px; background: var(--orange); }
  .front-body {
    position: absolute; left: 0; right: 0; top: 212px; bottom: 0;
    background: linear-gradient(180deg, var(--navy) 0%, var(--navy-soft) 55%, var(--navy-deep) 100%);
  }
  .ribbon {
    position: absolute; left: 40px; right: 20px; top: 192px; height: 34px;
    background: var(--orange); border-radius: 6px 6px 0 0;
    color: var(--ink); font-weight: 700; font-size: 16px; letter-spacing: 1.2px;
    white-space: nowrap;
    display: flex; align-items: center; justify-content: center;
  }
  .photo-strip {
    position: absolute; display: flex; gap: 3px;
    background: var(--paper); padding: 3px;
  }
  .card--front .photo-strip { left: 40px; right: 20px; top: 226px; height: 178px; }
  .photo { flex: 1; height: 100%; }
  .photo--wood-kitchen { background: linear-gradient(160deg, #d9c3a0 0%, #7a4a28 45%, #3a2416 100%); flex: 1.05; }
  .photo--shower { background: linear-gradient(180deg, #cfc7b8 0%, #9a8d78 50%, #6b6254 100%); flex: 0.85; }
  .photo--great-room { background: linear-gradient(170deg, #e8c88f 0%, #b07a45 45%, #5a3a22 100%); flex: 1.5; }
  .front-copy {
    position: absolute; left: 0; right: 0; top: 416px;
    text-align: center; color: var(--paper);
  }
  .front-copy .question { font-size: 19px; line-height: 1.25; letter-spacing: 0.3px; white-space: nowrap; }
  .front-copy .web { margin-top: 10px; font-size: 13px; font-weight: 600; letter-spacing: 1.2px; }

  /* ---------- Back ---------- */
  .card--back { left: 620px; top: 250px; height: 480px; }
  .back-intro { text-align: center; color: var(--ink); padding: 26px 14px 0; white-space: nowrap; }
  .back-intro .lead { font-weight: 600; font-size: 17px; }
  .back-intro .lead-strong { font-weight: 700; font-size: 22px; margin-top: 2px; }
  .back-intro .invite { font-style: italic; font-weight: 500; font-size: 16px; line-height: 1.3; margin-top: 10px; }
  .contact-band {
    position: absolute; left: 0; right: 0; top: 156px; height: 110px;
    background: linear-gradient(180deg, var(--orange) 0%, var(--orange-deep) 100%);
    border-top-right-radius: 10px;
    display: flex; align-items: center;
  }
  .band-mark {
    width: 70px; margin-left: 18px; text-align: center;
    color: var(--navy); font-weight: 600; font-size: 12px; line-height: 1.15;
  }
  .contact {
    flex: 1; text-align: center; color: var(--ink); padding-right: 10px; white-space: nowrap;
  }
  .contact .lines { font-size: 17px; font-weight: 500; }
  .contact .web { font-size: 21px; font-weight: 700; letter-spacing: 0.2px; margin-top: 2px; }
  .contact .mail { font-size: 12.5px; font-weight: 600; margin-top: 2px; }
  .socials { display: flex; gap: 4px; justify-content: center; margin-top: 5px; }
  .socials span { width: 14px; height: 14px; border-radius: 3px; background: var(--navy-soft); }
  .back-body {
    position: absolute; left: 0; right: 0; top: 266px; bottom: 0;
    background: linear-gradient(180deg, var(--navy) 0%, var(--navy-soft) 60%, var(--navy-deep) 100%);
  }
  .card--back .photo-strip { left: 12px; right: 12px; top: 262px; height: 118px; }
  .photo--white-kitchen { background: linear-gradient(170deg, #f0ede6 0%, #b8ab92 50%, #4a3d30 100%); flex: 1.1; }
  .photo--bath { background: linear-gradient(180deg, #f2e6d0 0%, #d4bd98 50%, #a48a66 100%); flex: 1; }
  .photo--tile-kitchen { background: linear-gradient(160deg, #3a2a20 0%, #5d7c93 45%, #8a5a32 100%); flex: 1.3; }
  .back-copy {
    position: absolute; left: 0; right: 0; top: 394px;
    text-align: center; color: var(--paper); white-space: nowrap;
    font-style: italic; font-weight: 500; font-size: 16px; line-height: 1.3;
  }
</style>
</head>
<body>

  <article class="card card--front">
    <header class="front-header">
      <div class="brand"><span class="brand-mark"></span>Beltridge Home Works</div>
    </header>
    <div class="front-body"></div>
    <div class="ribbon">WE ARE WORKING IN YOUR NEIGHBORHOOD!</div>
    <div class="photo-strip">
      <div class="photo photo--wood-kitchen" role="img" aria-label="Remodeled kitchen with wood cabinets, island and bar stools"></div>
      <div class="photo photo--shower" role="img" aria-label="Tiled walk-in shower with glass door"></div>
      <div class="photo photo--great-room" role="img" aria-label="Open kitchen with granite island and pendant lights"></div>
    </div>
    <div class="front-copy">
      <p class="question">Ever question the references you get from a contractor?<br>Wouldn't you prefer to get a reference from your neighbor?</p>
      <p class="web">WWW.BELTRIDGEHOMEWORKS.EXAMPLE</p>
    </div>
  </article>

  <article class="card card--back">
    <section class="back-intro">
      <p class="lead">We are currently working with one of your neighbors</p>
      <p class="lead-strong">and would love the opportunity to work for you.</p>
      <p class="invite">You can look us up on our website and see<br>some of the wonderful spaces we have helped create.</p>
    </section>
    <div class="back-body"></div>
    <section class="contact-band">
      <div class="band-mark">Beltridge Home Works</div>
      <div class="contact">
        <p class="lines">Tel: 555-302-1186 Fax:555-317-2094</p>
        <p class="web">WWW.BELTRIDGEHOMEWORKS.EXAMPLE</p>
        <p class="mail">BELTRIDGEHOMEWORKS@MAILBOXLY.EXAMPLE</p>
        <div class="socials"><span></span><span></span><span></span></div>
      </div>
    </section>
    <div class="photo-strip">
      <div class="photo photo--white-kitchen" role="img" aria-label="White kitchen with granite counters and window"></div>
      <div class="photo photo--bath" role="img" aria-label="Bathroom with white vanity, tub and shower"></div>
      <div class="photo photo--tile-kitchen" role="img" aria-label="Kitchen with blue glass tile backsplash and range"></div>
    </div>
    <p class="back-copy">Call us today to schedule an appointment and let us know<br>how we can help you create the new space<br>you have always dreamed of.</p>
  </article>

</body>
</html>
```